Below Par Parenting

I would like a poster (size to be agreed) created for the wording that I have composed and which I have pasted below. The poster is for my own personal gratification. It is not for commercial use. The message is driven by honesty and a profound sense of mea culpa. I am open to ideas regarding style and presentation.
I am an awful parent. No question. I am not cut out for this shit. I’m too quick to temper. I turn everything into a test of wills. I’m not down for food on the floor, for having my car trashed with your stink and detritus, for having the walls of my house daubed in your greasy fingerprints. I want to listen to The Marrows not Up the Paper Ladder on repeat. I enjoyed making you but, on reflection, I should have pulled out. Let me go back in time to that great waste of space and energy that is ante-natal classes and tell that boho with the flowery dress and curly hair, ‘Why are you concentrating on the first five seconds? All the pain comes later. Why aren’t you telling us what to do when they won’t sleep, when they won’t sit in their high chairs, when they won’t sleep on the aeroplane?’ Boy, I wish I could play it loosey-goosey like those left-leaning parents I see going ‘coo-coo’ in Benvolti’s but I’m not built like that. I am a right-wing despot. It’s Nazi Germany back at my place. I’m not interested in your meltdowns and tantrums. You want to writhe on the floor in the car park going red in the face? Make my day. You want to go spastic because I won’t let you watch TV for five hours straight? I don’t give a shit. Read my lips. I won’t pander to it. My wife says you’re babies but all I see is little people with an agenda. I’ve got naughty steps and sin-bins all over the joint. I wish I wasn’t the tyrant, the Valdarrez and the Okoro Tembe I am but it is what it is. I blame my parents and they, in turn, will blame me and their parents. Understand I don’t want to infect you too much with my bad behavior but if you could stop making such a scene in public places with your screaming, your bitching and your all round refusal to play nice then maybe, just maybe, we’d have a chance and I wouldn’t be such an awful parent.

```html
<!DOCTYPE html>
<html lang="en">
<head>
<meta charset="utf-8">
<title>I Am An Awful Parent</title>
<link rel="stylesheet" href="https://fonts.googleapis.com/css2?family=Caveat:wght@400;700&family=Special+Elite&display=swap">
<style>
  :root {
    --backdrop: #e9e9e7;
    --paper: #fbfbfa;
    --rule: #dcdfe4;
    --ink: #1d1d1d;
    --ink-red: #c8142c;
    --ink-blue: #3346c2;
    --tape: #c9a978;
    --jam: #b3121c;
    --crumb: #6b4a33;
    --sketch-light: #f1f1ef;
    --sketch-mid: #e2e2df;
  }
  html, body {
    margin: 0;
    width: 1200px;
    height: 900px;
    overflow: hidden;
    background: var(--backdrop);
  }
  .poster {
    position: absolute;
    left: 300px;
    top: 12px;
    width: 600px;
    height: 876px;
    background:
      repeating-linear-gradient(to bottom, transparent 0 32px, var(--rule) 32px 33px) 0 10px / 100% 100%,
      var(--paper);
    box-shadow: 0 2px 8px rgba(0,0,0,.18);
    overflow: hidden;
    font-family: "Caveat", cursive;
    color: var(--ink);
  }
  .jam-splatter {
    position: absolute;
    right: 0;
    top: 0;
    width: 110px;
    height: 70px;
    background: radial-gradient(circle at 70% 35%, var(--jam) 0 28%, rgba(179,18,28,.35) 45%, transparent 68%);
  }
  .letter {
    position: absolute;
    left: 32px;
    top: 60px;
    width: 548px;
    margin: 0;
    font-size: 15px;
    line-height: 33px;
  }
  .line {
    display: block;
    white-space: nowrap;
  }
  .title {
    font-family: "Special Elite", monospace;
    font-size: 15px;
    letter-spacing: 1px;
    background: var(--tape);
    padding: 1px 4px;
    margin-right: 3px;
  }
  .strong { font-weight: 700; }
  .red { color: var(--ink-red); }
  .blue { color: var(--ink-blue); }
  .underline { text-decoration: underline; text-decoration-thickness: 1.5px; text-underline-offset: 3px; }
  .tantrum-doodle {
    position: absolute;
    left: 516px;
    top: 440px;
    width: 66px;
    height: 70px;
    border-radius: 50%;
    background: radial-gradient(circle, rgba(200,20,44,.28), rgba(200,20,44,.08) 68%, transparent 72%);
  }
  .family-sketch {
    position: absolute;
    left: 40px;
    top: 676px;
    width: 530px;
    height: 168px;
    background: linear-gradient(to bottom, var(--sketch-light), var(--sketch-mid));
    border-radius: 6px;
  }
  .flower-border {
    position: absolute;
    left: 40px;
    top: 852px;
    width: 530px;
    height: 10px;
    background: var(--sketch-mid);
    border-radius: 5px;
  }
  .crumb {
    position: absolute;
    width: 10px;
    height: 9px;
    border-radius: 45%;
    background: var(--crumb);
  }
</style>
</head>
<body>
  <main class="poster">
    <div class="jam-splatter" role="img" aria-label="Jam splatter stains in the top corner"></div>
    <span class="crumb" style="left:70px;top:36px"></span>
    <span class="crumb" style="left:548px;top:420px"></span>
    <span class="crumb" style="left:262px;top:702px"></span>

    <p class="letter">
      <span class="line"><span class="title">I AM AN AWFUL PARENT</span> <span class="strong underline">No question.</span> I am not cut out for this shit. I’m too</span>
      <span class="line"><span class="strong">quick to temper</span>, too ready to go Nagasaki. I’m not down for food on the floor, for having <span class="underline">my car smeared</span></span>
      <span class="line">with your stink and detritus, for having the walls of my house daubed in your <span class="strong">bolognaise fingerprints.</span></span>
      <span class="line">I want to listen to <span class="red">Hollow Pylons</span> not Up the Paper Ladder on repeat. <span class="strong">I enjoyed making you</span> but on</span>
      <span class="line">reflection I should have <span class="strong">pulled out.</span> Let me go back in time to that great waste of space and energy</span>
      <span class="line">that was ante-natal classes and tell that boho with the flowery dress, ‘Why are you <span class="strong">concentrating</span></span>
      <span class="line">on the labour? All the hard work comes later.’ <span class="blue">Boy, <span class="underline">I wish</span></span> I could play it loosey-goosey like those</span>
      <span class="line">left-leaning parents I see going ‘coo-coo’ in Benvolti’s <span class="strong">but I’m not built like that.</span> I am a right-wing</span>
      <span class="line">despot. It’s Guantanamo Bay back at <span class="underline">my place</span> with a sin bin here and a naughty step there. I’m not</span>
      <span class="line">interested in your <span class="red">meltdowns and tantrums.</span> <span class="strong">You want to writhe on the floor</span> in the car park going</span>
      <span class="line">red in the face? Make my day. You want to go <span class="strong">spastic</span> because <span class="strong">I won’t let you watch TV</span> for five hours</span>
      <span class="line">straight? I don’t give a shit. <span class="red underline">Read my lips.</span> I won’t pander to it. <span class="strong">My wife says</span> you’re babies</span>
      <span class="line">but all I see is <span class="strong">little people with an agenda</span> and their own language. <span class="red">What is it that you speak?</span></span>
      <span class="line">Hutu with Hebrew? Damn, I wish I wasn’t the tyrant, the Valdarrez and the Okoro Tembe</span>
      <span class="line">I am but it is what it is. <span class="strong underline">But who am I kidding?</span> You don’t respect me or my mortgage. I can’t pooh in</span>
      <span class="line">the bath like you do. (I pee but that’s not the same) You’re up with there with Rory Vance leaving your</span>
      <span class="line">bedroom looking like the Tet Offensive. <span class="red">I give up.</span> I sue for peace. Hartwell style. I’ll be downstairs</span>
      <span class="line">beaten with a whisky. Do as you please. I can’t control you but know that <span class="red strong underline">I’m here if you need me.</span></span>
    </p>

    <div class="tantrum-doodle" role="img" aria-label="Red doodle of a screaming toddler head with devil horns"></div>
    <div class="family-sketch" role="img" aria-label="Pencil sketch of a father running away, a crying toddler on the floor, an empty cot and a mother in a dressing gown"></div>
    <div class="flower-border" role="img" aria-label="Row of small doodled flowers along the bottom edge"></div>
  </main>
</body>
</html>
```